Commercial Broker Profile Flyer

I need a one-page flyer created that will serve as a profile report for individual brokers within a commercial real estate firm. The flyer will include company branding, agent photo, bio, and other information. I would like to have the source file available for future editing preferably in a Publisher file format. A copy of a company brochure is included and would like to have this profile flyer similar to keep company branding consistent. Our company website is www.holbrookvalere.com for any other questions on branding.
Updates

Target Market(s)

Professional

Industry/Entity Type

Real Estate Agent

Requirements
Must have
• One page
• Source files MUST include a .PUB file that I can update in the future
• All of the information in the uploaded "content" file
• Company branding
• Must be 8.5"x11"
Should not have
• Do not use stock photos or property photos from the attachments. I only want the broker photo and company logo.

```html
<!DOCTYPE html>
<html lang="en">
<head>
<meta charset="utf-8">
<title>Broker Profile – Holbrook Valere Real Estate</title>
<link href="https://fonts.googleapis.com/css2?family=Open+Sans:wght@300;400;600;700&display=swap" rel="stylesheet">
<style>
  :root {
    --green-dark: #0b6a3c;
    --green-light: #5fae3b;
    --ink: #2b2b2b;
    --ink-soft: #444;
    --frame: #e4e4e4;
    --paper: #ffffff;
  }
  * { box-sizing: border-box; margin: 0; padding: 0; }
  html, body { width: 1056px; height: 1200px; overflow: hidden; background: var(--paper); }
  body { font-family: "Open Sans", Arial, sans-serif; color: var(--ink); position: relative; }

  .page-frame { position: absolute; left: 72px; top: 10px; width: 912px; height: 1180px; border: 1px solid var(--frame); }

  .brand { position: absolute; left: 577px; top: 66px; display: flex; align-items: center; gap: 10px; color: var(--green-dark); }
  .brand-dot { width: 74px; height: 74px; border-radius: 50%; background: var(--green-dark); flex: none; }
  .brand-name { display: block; font-weight: 600; font-size: 31px; line-height: 1; }
  .brand-sub { display: block; font-weight: 600; font-size: 15px; letter-spacing: 7px; margin-top: 8px; padding-left: 26px; }

  .portrait { position: absolute; left: 151px; top: 144px; width: 234px; height: 290px; }

  .contact { position: absolute; left: 412px; top: 278px; font-size: 14.6px; line-height: 22.6px; color: var(--ink-soft); }
  .contact-name { font-size: 17.5px; line-height: 24px; margin-bottom: 1px; }
  .contact-name strong { color: var(--green-dark); font-weight: 700; }
  .contact-line { display: flex; align-items: center; gap: 9px; }
  .contact-line svg { width: 13px; height: 13px; flex: none; }

  .bio { position: absolute; left: 149px; top: 474px; width: 720px; font-size: 16.2px; line-height: 20.8px; font-weight: 300; color: var(--ink); }
  .bio p + p { margin-top: 7px; }

  .section-head { position: absolute; left: 146px; width: 629px; height: 28px; border-bottom: 2px solid var(--green-dark); }
  .section-head span { display: inline-block; height: 28px; padding: 0 7px; background: var(--green-dark); color: #fff; font-weight: 700; font-size: 19.5px; line-height: 28px; letter-spacing: 0.3px; }
  .head-clients { top: 733px; }
  .head-affiliations { top: 922px; }

  .clients { position: absolute; left: 162px; top: 779px; display: grid; grid-template-columns: 169px 208px 240px; row-gap: 9px; font-size: 17.6px; line-height: 25px; font-weight: 600; color: #222; list-style: none; }

  .affiliations { position: absolute; left: 151px; top: 963px; list-style: none; font-size: 17.5px; font-weight: 300; color: #333; }
  .affiliations li { display: flex; align-items: center; gap: 8px; line-height: 30px; }
  .affiliations li::before { content: ""; width: 6px; height: 6px; border-radius: 50%; background: var(--green-dark); flex: none; }

  .footer-wave { position: absolute; left: 72px; top: 1090px; width: 912px; height: 100px; }
</style>
</head>
<body>
  <div class="page-frame"></div>

  <div class="brand">
    <div class="brand-dot"></div>
    <div>
      <span class="brand-name">Holbrook Valere</span>
      <span class="brand-sub">REAL ESTATE</span>
    </div>
  </div>

  <svg class="portrait" viewBox="0 0 264 288" preserveAspectRatio="none" role="img" aria-label="Broker headshot photograph">
    <defs>
      <linearGradient id="portraitFill" x1="0" y1="0" x2="1" y2="1">
        <stop offset="0" stop-color="#9a9e9c"/>
        <stop offset="1" stop-color="#6f7472"/>
      </linearGradient>
    </defs>
    <path d="M22 2 L228 30 Q262 35 262 70 L262 240 Q262 268 234 272 L26 286 Q2 288 2 262 L2 24 Q2 0 22 2 Z" fill="#fff" stroke="#c9c9c9" stroke-width="2"/>
    <path d="M26 12 L224 39 Q252 43 252 72 L252 236 Q252 258 230 261 L30 276 Q12 277 12 258 L12 30 Q12 10 26 12 Z" fill="url(#portraitFill)"/>
  </svg>

  <div class="contact">
    <p class="contact-name"><strong>R. Daniel Holbrook,</strong> CCPA, ALP</p>
    <p>Principal / Broker in Charge</p>
    <p>Office Phone: (555) 214-3870 ext. 118</p>
    <p class="contact-line">
      <svg viewBox="0 0 14 14"><rect width="14" height="14" rx="3" fill="var(--green-dark)"/><path d="M4 3.5c.5-.4 1-.3 1.3.2l.6 1.1c.2.4.1.8-.2 1l-.4.3c.4.9 1.1 1.6 2 2l.3-.4c.3-.3.7-.4 1-.2l1.1.6c.5.3.6.8.2 1.3-.6.8-1.5.9-2.4.4C5.8 9 4.8 8 4 6.3c-.4-1-.5-2 0-2.8z" fill="#fff"/></svg>
      555) 306-7142
    </p>
    <p class="contact-line">
      <svg viewBox="0 0 14 14"><rect x="1" y="2.5" width="12" height="9" rx="1.5" fill="none" stroke="var(--green-dark)" stroke-width="1.6"/><path d="M1.8 3.5 7 7.5l5.2-4" fill="none" stroke="var(--green-dark)" stroke-width="1.4"/></svg>
      daniel@holbrookvalere.com
    </p>
    <p class="contact-line">
      <svg viewBox="0 0 14 14"><circle cx="7" cy="7" r="6.2" fill="var(--green-dark)"/><path d="M1.5 7h11M7 1c-2.4 3.6-2.4 8.4 0 12M7 1c2.4 3.6 2.4 8.4 0 12M2.5 4h9M2.5 10h9" fill="none" stroke="#fff" stroke-width="0.9"/></svg>
      www.holbrookvalere.com
    </p>
  </div>

  <div class="bio">
    <p>Daniel began his real estate career in 2005 and has completed $75+ million in transactions representing sellers and buyers of commercial real estate, providing tenant representation, and leasing of retail and office properties. Prior to beginning his real estate career, Daniel served over five years in the Army Reserves and attended Eastbrook State University.</p>
    <p>Daniel has earned the prestigious Chartered Commercial Property Advisor (CCPA) designation as well as the Accredited Leasing Professional (ALP) designation. Daniel is a member of the Allied Council of Retail Centers (ACRC), the Carolina and Pinecrest Realtor Association, the Pinecrest-Marlow County Chamber of Commerce, and serves on the board of directors for the NC Commercial Investment Chapter, the Sandhill Community Fitness League, and the Tallpine Realtors Association. Daniel is a licensed real estate broker in NC and SC.</p>
  </div>

  <h2 class="section-head head-clients"><span>CLIENT SERVED</span></h2>
  <ul class="clients">
    <li>Copperleaf Grill</li><li>Roadline Tires</li><li>Kinward Services</li>
    <li>Brickyard Burgers</li><li>Petite Crumb</li><li>Main Street Media</li>
    <li>Fairway Cuts</li><li>Brightwell Home Care</li><li>Riverbend Beverage Group</li>
  </ul>

  <h2 class="section-head head-affiliations"><span>PROFESSIONAL AFFILIATIONS</span></h2>
  <ul class="affiliations">
    <li>Chartered Commercial Property Advisor (designee)</li>
    <li>Allied Council of Retail Centers</li>
    <li>Tallpine Realtors Association</li>
    <li>State Realtors Commercial Forms Committee</li>
  </ul>

  <svg class="footer-wave" viewBox="0 0 912 100" preserveAspectRatio="none" aria-hidden="true">
    <path d="M0 43 C300 62 520 12 680 6 C800 2 880 22 912 49 L912 100 L0 100 Z" fill="var(--green-dark)"/>
    <path d="M0 43 C300 62 520 12 680 6 C800 2 880 22 912 49" fill="none" stroke="var(--green-light)" stroke-width="4"/>
  </svg>
</body>
</html>
```